Dune Business Card Design Project

We have an existing business card. We are looking to creat a new card for the store. I have attached a my own business so you have a refference of what the current card looks like.

Phone: 1300 574 213
email: merrow@dunepanes.com.au
website: www.dunepanes.com.au
Address: (Inside Merrow Rug Hall) 418 Tolvey Rd, Pelbrook VIC 3158
Updates

This is a new business card for our store.

Industry/Entity Type

Business

Requirements
Must have
• Must look similar to the existing card

```html
<!DOCTYPE html>
<html lang="en">
<head>
<meta charset="utf-8">
<title>Dune Shutters &amp; Blinds – Business Card Options</title>
<link rel="stylesheet" href="https://fonts.googleapis.com/css2?family=Arimo:wght@400;700&display=swap">
<style>
  :root {
    --sheet: #ffffff;
    --sheet-border: #c8c8c8;
    --card: #fdfdfd;
    --card-border: #b9b9b9;
    --band: #edebe5;
    --ink: #2f2a2a;
    --tagline: #6b6b6b;
    --body: #4f4f4f;
    --accent-red: #e0202a;
    --dot-blue: #7ecff0;
    --dot-red: #e0202a;
    --dot-gold: #d4a80d;
  }
  * { box-sizing: border-box; margin: 0; padding: 0; }
  html, body { width: 715px; height: 1200px; overflow: hidden; background: var(--sheet); }
  body { font-family: "Arimo", Arial, sans-serif; color: var(--body); }

  .sheet {
    position: relative;
    width: 715px; height: 1200px;
    border: 1px solid var(--sheet-border);
    background: var(--sheet);
  }
  .option-number {
    position: absolute; left: 46px;
    font-size: 20px; color: #333;
  }
  .card {
    position: absolute;
    width: 547px; height: 337px;
    background: var(--card);
    border: 1px solid var(--card-border);
    box-shadow: 8px 10px 18px rgba(0,0,0,0.14);
    overflow: hidden;
  }
  .card--one { left: 82px; top: 57px; }
  .card--two { left: 79px; top: 415px; }
  .card--back { left: 80px; top: 774px; }

  .info-band {
    position: absolute; left: 0; right: 0; bottom: 0;
    background: var(--band);
  }
  .card--one .info-band { top: 185px; }
  .card--two .info-band { top: 186px; }

  .brand { position: absolute; color: var(--ink); }
  .brand__name {
    display: block;
    font-weight: 400;
    line-height: 1;
    letter-spacing: -1px;
    color: var(--ink);
  }
  .brand__tagline {
    display: block;
    font-weight: 700;
    color: var(--tagline);
  }
  .card--one .brand { left: 40px; top: 52px; }
  .card--one .brand__name { font-size: 82px; }
  .card--one .brand__tagline { font-size: 17px; margin-top: 6px; }

  .card--two .brand { left: 0; right: 0; top: 16px; text-align: center; }
  .card--two .brand__name { font-size: 76px; }
  .card--two .brand__tagline { font-size: 16px; margin-top: 4px; }

  .card--back .brand { left: 0; right: 0; top: 66px; text-align: center; }
  .card--back .brand__name { font-size: 118px; }
  .card--back .brand__tagline { font-size: 22px; margin-top: 8px; }

  .web-line {
    position: absolute; left: 0; right: 0; top: 245px;
    text-align: center;
    font-size: 16px; letter-spacing: 1px; color: #3a3a3a;
  }

  .service-icons { position: absolute; display: flex; gap: 23px; }
  .service-icons svg { width: 36px; height: 36px; display: block; }
  .card--one .service-icons { left: 38px; top: 201px; }
  .card--two .service-icons { left: 201px; top: 130px; }

  .contact-list { position: absolute; list-style: none; font-size: 13px; line-height: 22.7px; color: var(--body); }
  .contact-list li { position: relative; padding-left: 24px; }
  .contact-list li::before {
    content: ">>"; position: absolute; left: 0; top: 0;
    color: var(--accent-red); font-size: 11px;
  }
  .contact-list li.continued::before { content: none; }
  .card--one .contact-list { left: 220px; top: 200px; }
  .card--two .contact-list { left: 130px; top: 200px; }
</style>
</head>
<body>
<main class="sheet">

  <span class="option-number" style="top:264px">1</span>
  <section class="card card--one" aria-label="Front option 1">
    <div class="brand">
      <span class="brand__name">Dune</span>
      <span class="brand__tagline">Shutters &amp; Blinds</span>
    </div>
    <div class="info-band"></div>
    <div class="service-icons">
      <svg viewBox="0 0 36 36"><circle cx="18" cy="18" r="16.5" fill="none" stroke="var(--dot-blue)" stroke-width="2"/><circle cx="18" cy="18" r="12.5" fill="var(--dot-blue)"/><path d="M11 18h13M19 12.5l5.5 5.5-5.5 5.5" fill="none" stroke="#fff" stroke-width="2.4" stroke-linecap="round" stroke-linejoin="round"/></svg>
      <svg viewBox="0 0 36 36"><circle cx="18" cy="18" r="16.5" fill="none" stroke="var(--dot-red)" stroke-width="2"/><circle cx="18" cy="18" r="12.5" fill="var(--dot-red)"/><path d="M11 18h13M19 12.5l5.5 5.5-5.5 5.5" fill="none" stroke="#fff" stroke-width="2.4" stroke-linecap="round" stroke-linejoin="round"/></svg>
      <svg viewBox="0 0 36 36"><circle cx="18" cy="18" r="16.5" fill="none" stroke="var(--dot-gold)" stroke-width="2"/><circle cx="18" cy="18" r="12.5" fill="var(--dot-gold)"/><path d="M11 18h13M19 12.5l5.5 5.5-5.5 5.5" fill="none" stroke="#fff" stroke-width="2.4" stroke-linecap="round" stroke-linejoin="round"/></svg>
    </div>
    <ul class="contact-list">
      <li>Phone: 1300 574 213</li>
      <li>Email: merrow@dunepanes.com.au</li>
      <li>Address: (Inside Merrow Rug Hall)</li>
      <li class="continued">418 Tolvey Rd, Pelbrook VIC 3158</li>
      <li>Website: www.dunepanes.com.au</li>
    </ul>
  </section>

  <span class="option-number" style="top:602px">2</span>
  <section class="card card--two" aria-label="Front option 2">
    <div class="info-band"></div>
    <div class="brand">
      <span class="brand__name">Dune</span>
      <span class="brand__tagline">Shutters &amp; Blinds</span>
    </div>
    <div class="service-icons">
      <svg viewBox="0 0 36 36"><circle cx="18" cy="18" r="16.5" fill="none" stroke="var(--dot-blue)" stroke-width="2"/><circle cx="18" cy="18" r="12.5" fill="var(--dot-blue)"/><path d="M11 18h13M19 12.5l5.5 5.5-5.5 5.5" fill="none" stroke="#fff" stroke-width="2.4" stroke-linecap="round" stroke-linejoin="round"/></svg>
      <svg viewBox="0 0 36 36"><circle cx="18" cy="18" r="16.5" fill="none" stroke="var(--dot-red)" stroke-width="2"/><circle cx="18" cy="18" r="12.5" fill="var(--dot-red)"/><path d="M11 18h13M19 12.5l5.5 5.5-5.5 5.5" fill="none" stroke="#fff" stroke-width="2.4" stroke-linecap="round" stroke-linejoin="round"/></svg>
      <svg viewBox="0 0 36 36"><circle cx="18" cy="18" r="16.5" fill="none" stroke="var(--dot-gold)" stroke-width="2"/><circle cx="18" cy="18" r="12.5" fill="var(--dot-gold)"/><path d="M11 18h13M19 12.5l5.5 5.5-5.5 5.5" fill="none" stroke="#fff" stroke-width="2.4" stroke-linecap="round" stroke-linejoin="round"/></svg>
    </div>
    <ul class="contact-list">
      <li>Phone: 1300 574 213</li>
      <li>Email: merrow@dunepanes.com.au</li>
      <li>Address: (Inside Merrow Rug Hall)</li>
      <li class="continued">418 Tolvey Rd, Pelbrook VIC 3158</li>
      <li>Website: www.dunepanes.com.au</li>
    </ul>
  </section>

  <section class="card card--back" aria-label="Card back">
    <div class="brand">
      <span class="brand__name">Dune</span>
      <span class="brand__tagline">Shutters &amp; Blinds</span>
    </div>
    <p class="web-line">www.dunepanes.com.au</p>
  </section>

</main>
</body>
</html>
```